Therapeutic Counselling Practice Brochure

I have a new therapeutic counselling practice in Melbourne.

I am making peri natal issues my special interest area.

I need a brochure targeted at new parents or pregnant women and partners, struggling with the concept of parenting, depression, maybe do not even know about it.

The feel should be safe and strong. I love the KOALIN website ( I do volunteer work with them)

Out of hours appointments and telephone counselling are important making my service very accessible.

Attached is an example for the content of the Brochure
Updates

Attached is an example for the content of the Brochure.

Target Market(s)

25 - 45 New Parents , expectant parents,families and friends of people struggling emotionally and mentally with and around being new parents

Industry/Entity Type

Work

Requirements
Must have
• Feel of safety, somewhere to go for help, support, a conversation, soft ,strong
Nice to have
• mother and child, maybe parents and child, possibly a graphic, faceless

```html
<!DOCTYPE html>
<html lang="en">
<head>
<meta charset="utf-8">
<title>Miriam Ashcombe – Perinatal Counselling Brochure</title>
<link href="https://fonts.googleapis.com/css2?family=Raleway:wght@300;400;500;700&family=Libre+Baskerville:ital,wght@1,400&display=swap" rel="stylesheet">
<style>
  :root{
    --pink:#d62f6a;
    --pink-deep:#b7245a;
    --white:#ffffff;
    --paper:#fbf8f8;
    --ink:#4a3a40;
    --backdrop:#ccd3db;
  }
  *{box-sizing:border-box;margin:0;padding:0}
  html,body{width:1168px;height:1200px;overflow:hidden}
  body{background:var(--backdrop);font-family:'Raleway',sans-serif;color:var(--white);
    display:flex;flex-direction:column;align-items:center;justify-content:center;gap:16px}
  .spread{display:grid;grid-template-columns:repeat(3,270px);height:572px;
    box-shadow:0 6px 18px rgba(60,70,90,.25)}
  .panel{background:var(--pink);display:flex;flex-direction:column;position:relative;
    border-right:1px solid rgba(0,0,0,.08);overflow:hidden}
  .panel:last-child{border-right:none}
  .caps{text-transform:uppercase;font-weight:300;letter-spacing:.02em;text-align:center;line-height:1.25}
  .italic{font-family:'Libre Baskerville',serif;font-style:italic;font-size:9.2px;line-height:1.5}
  .band{background:var(--pink-deep);padding:16px 18px}
  .body-copy{padding:16px 18px;display:flex;flex-direction:column;gap:9px}
  .brand{margin-top:auto;padding:16px 18px 22px;display:flex;flex-direction:column;align-items:center;gap:4px}
  .brand-rule{width:170px;height:1px;background:var(--white);opacity:.9}
  .brand-name{display:flex;align-items:center;gap:7px;font-size:17px;font-weight:300;letter-spacing:.04em}
  .brand-dot{width:8px;height:8px;border-radius:50%;background:var(--white)}
  .brand-tag{font-size:8px;font-weight:300;letter-spacing:.08em}
  .photo{display:block}
  .photo-sky{height:80px;margin:16px 18px 0;background:linear-gradient(180deg,#2f6fc2,#8fb7e6 60%,#e8f0fa)}
  .photo-sunset{width:76px;height:66px;flex-shrink:0;background:linear-gradient(180deg,#f0b46a,#9a5a3a 60%,#2a1a16)}
  .photo-portrait{height:160px;margin:10px 14px 0;background:linear-gradient(120deg,#e9e3dc,#c7a894 45%,#5f7a3c)}
  .cover-art{height:300px;margin:22px 40px 0;border-radius:4px;
    background:radial-gradient(ellipse at 45% 40%,rgba(255,255,255,.35),rgba(255,255,255,.05) 70%)}
  .cover-head{font-size:15px;margin-bottom:8px}
  .cover-lead{font-size:10.5px;text-align:center;line-height:1.35;font-weight:400}
  .quote{font-size:10.5px;padding:20px 18px}
  .list{list-style:none;display:flex;flex-direction:column;gap:3px;padding-left:4px}
  .list li::before{content:"• "}
  .sub{font-size:11.5px;margin-bottom:7px}
  .small-sans{font-size:9px;line-height:1.5;text-align:center;font-weight:400}
  .term{font-weight:700}
  .contact-top{background:var(--pink-deep);padding:7px;font-size:10px}
  .contact-paper{background:var(--paper);color:var(--ink);padding-bottom:12px}
  .address{font-size:7.5px;text-transform:uppercase;margin:8px 14px 4px;letter-spacing:.03em}
  .accent{color:var(--pink);font-size:9px;margin:0 14px 4px}
  .contact-paper .italic{margin:0 14px 4px;color:var(--ink);font-size:8.6px}
  .contact-name{font-size:16px;margin:3px 0}
  .contact-line{font-size:11px}
  .muted{font-size:8px;margin-top:4px}
  .mid-top{display:flex;gap:8px;padding:16px 14px 0}
  .mid-head{font-size:9.5px;text-align:left}
  .split-head{display:flex;justify-content:space-between;font-size:10px}
  .stat{font-size:10.5px}
</style>
</head>
<body>

<section class="spread" aria-label="Brochure outside">
  <article class="panel">
    <div class="photo photo-sky" role="img" aria-label="Photo of blue sky with soft white clouds"></div>
    <div class="body-copy italic">
      <p>Depression impacts on the whole family, including baby.</p>
      <p>You may feel guilty and a "not good enough mother"; you may lose confidence.</p>
      <p>Depression can be treated with counselling, "talk therapy".</p>
      <p>A check up at your doctor is advisable too.</p>
      <p>Postpartum depression doesn't discriminate.</p>
      <p>It affects women of all ages, cultural and social standing.</p>
    </div>
    <div class="band caps quote">"Sometimes," said a wise friend,<br>"the smallest thing takes up the most room in your heart."</div>
    <div class="brand">
      <span class="brand-rule"></span>
      <span class="brand-name"><span class="brand-dot"></span>Miriam Ashcombe</span>
      <span class="brand-tag">Counsellor and Personal Coach</span>
    </div>
  </article>

  <article class="panel">
    <div class="body-copy italic">
      <p>The good news is that most women who seek help recover well and go on to enjoy being a parent.</p>
      <p>If you have any of the following symptoms for more than two weeks, please talk to someone:</p>
      <ul class="list">
        <li>Feeling sad, low or teary</li>
        <li>Feeling anxious or on edge</li>
        <li>Trouble sleeping, even when tired</li>
        <li>Loss of interest in things you enjoy</li>
        <li>Feeling numb or disconnected</li>
        <li>Changes in appetite</li>
        <li>Thoughts of harming yourself or baby</li>
        <li>Feeling you are not coping</li>
      </ul>
    </div>
    <div class="band">
      <h2 class="caps sub">Depression<br>during and after pregnancy</h2>
      <p class="small-sans">Depression is more than the baby blues. It can start in pregnancy or in the first year after birth and may come slowly or all at once.</p>
    </div>
    <div class="brand">
      <span class="brand-rule"></span>
      <span class="brand-name"><span class="brand-dot"></span>Miriam Ashcombe</span>
      <span class="brand-tag">Counsellor and Personal Coach</span>
    </div>
  </article>

  <article class="panel">
    <div class="cover-art" role="img" aria-label="Line illustration of a mother holding her baby"></div>
    <div class="band" style="margin-top:22px">
      <h1 class="caps cover-head">Are you expecting or a new parent? Got the baby blues?</h1>
      <p class="cover-lead">There is an expectation of happiness and fulfilment around childbirth. Feeling 'blue' interferes with the adjustment to becoming a parent. Sharing your feelings by talking is important.</p>
    </div>
    <div class="brand">
      <span class="brand-rule"></span>
      <span class="brand-name"><span class="brand-dot"></span>Miriam Ashcombe</span>
      <span class="brand-tag">Counsellor and Personal Coach</span>
    </div>
  </article>
</section>

<section class="spread" aria-label="Brochure inside">
  <article class="panel">
    <div class="body-copy italic">
      <h2 class="caps sub" style="font-family:'Raleway',sans-serif;font-style:normal">Looking after yourself</h2>
      <p><span class="term">Rest</span><br>Sleep if you can, and have a rest if you can't. Nap when your baby is sleeping.</p>
      <p><span class="term">Eat</span><br>Eat a healthy, well-balanced diet. Keep snacks close by and water handy.</p>
      <p><span class="term">Exercise</span><br>A gentle walk each day helps you feel better in body and mind.</p>
      <p><span class="term">Meditate</span><br>It may be difficult to quieten your mind; a guided meditation can help.</p>
      <p><span class="term">Stay connected</span><br>Having a baby can make you feel isolated. Meet with other new parents.</p>
      <p><span class="term">Be kind to yourself</span><br>Don't load yourself with things that really don't need to be done.</p>
    </div>
    <div class="band">
      <h3 class="split-head caps"><span>Help</span><span>Ask and accept</span></h3>
      <p class="small-sans" style="margin-top:6px">Ask and accept offers of help around the home and with meals. You may not need professional help all the moment; surround yourself with people you can be honest with.</p>
    </div>
    <div class="brand">
      <span class="brand-rule"></span>
      <span class="brand-name"><span class="brand-dot"></span>Miriam Ashcombe</span>
      <span class="brand-tag">Counsellor and Personal Coach</span>
    </div>
  </article>

  <article class="panel">
    <div class="mid-top">
      <div class="photo photo-sunset" role="img" aria-label="Photo of a parent and child silhouetted at sunset"></div>
      <h2 class="caps mid-head">Depression after the birth of a child affects fathers too</h2>
    </div>
    <div class="body-copy italic">
      <p>For new dads the focus is often on mother and baby, and their own feelings are overlooked or pushed aside.</p>
      <p>Symptoms can include feeling irritable, withdrawn, working longer hours or drinking more than usual.</p>
      <p>Connecting can help. Talking with a counsellor gives you a safe and confidential space.</p>
    </div>
    <div class="band">
      <p class="caps stat">According to recent research about 1 in 10 new fathers become depressed after the birth of their child</p>
      <p class="small-sans" style="margin-top:6px">www.koalin.org.au</p>
    </div>
    <div class="brand">
      <span class="brand-rule"></span>
      <span class="brand-name"><span class="brand-dot"></span>Miriam Ashcombe</span>
      <span class="brand-tag">Counsellor and Personal Coach</span>
    </div>
  </article>

  <article class="panel">
    <div class="contact-top caps">Miriam Ashcombe, JP</div>
    <div class="contact-paper">
      <div class="photo photo-portrait" role="img" aria-label="Portrait photo of the counsellor outdoors among green leaves"></div>
      <p class="address">Office: 14 Harlow Street, Brindle Vale 3190</p>
      <p class="accent">Evening and weekend appointments available</p>
      <p class="italic">Telephone counselling saves travel time and the hassle of parking. Some people feel more able to share over the telephone, still within a safe and confidential framework.</p>
      <p class="accent">Appointments are usually available within 48 hours</p>
    </div>
    <div class="band caps">
      <p class="contact-line" style="font-size:9px">To book please contact</p>
      <p class="contact-name">Miriam Ashcombe</p>
      <p class="contact-line">on 0412 555 318</p>
      <p class="muted">miriam@miriamashcombe.com.au</p>
      <p class="muted" style="margin-top:1px">www.miriamashcombe.com.au</p>
    </div>
    <div class="brand">
      <span class="brand-rule"></span>
      <span class="brand-name"><span class="brand-dot"></span>Miriam Ashcombe</span>
      <span class="brand-tag">Counsellor and Personal Coach</span>
    </div>
  </article>
</section>

</body>
</html>
```